College Admissions Consulting needs a small street facing sign for new office location.

I need a graphic design to be used inside window for a banner/sign in office location on a high walking traffic city street, for my company, Campus Lantern. I work with high school students and families on the college planning and selection application process. Please check out the website to learn more about what I do (www.mycampuslantern.example). The banner will be used to market our services at our office location. The final design should utilize logo colors, phone number, and website/email information. I'd like to incorporate a my picture in someway because of face recognition. To be printed on a posterboard or vinyl banner.

Target Market(s)

Parents of high school aged children.

Industry/Entity Type

Education

Font styles to use
Sans Serif

Colors
abd037

Requirements
Must have
• Clean, attractive, and professional design. Attract the attention of people walking by. Information must be clear and readable (phone/email, etc.).
Nice to have
• Utilize the picture with crossed arms (without the brown background on picture).
Emphasize tagline:
Mastering The College Admission Process
....with personalized, professional guidance in planning, selecting, and applying to the right colleges.

```html
<!DOCTYPE html>
<html lang="en">
<head>
<meta charset="utf-8">
<title>Campus Lantern – Window Banner</title>
<link rel="stylesheet" href="https://fonts.googleapis.com/css2?family=Poppins:wght@600;700&family=Questrial&display=swap">
<style>
  :root {
    --green: #8cc63f;
    --charcoal: #4a4a4c;
    --ink: #3b3b3d;
    --paper: #ffffff;
    --stage: #e2e2e1;
    --tab: #e6e6e6;
    --photo-light: #9a9a9a;
    --photo-dark: #2a2a2a;
  }
  * { margin: 0; padding: 0; box-sizing: border-box; }
  html, body {
    width: 1200px; height: 858px; overflow: hidden;
    background: var(--stage);
  }
  .banner {
    position: absolute; left: 125px; top: 112px;
    width: 950px; height: 633px;
    background: var(--paper);
    box-shadow: 6px 8px 10px rgba(0,0,0,.35);
    overflow: hidden;
    font-family: "Questrial", sans-serif;
  }
  .banner-shapes { position: absolute; inset: 0; }
  .brand {
    position: absolute; left: 52px; top: 34px;
    display: flex; align-items: center; gap: 16px;
  }
  .brand-dot {
    width: 62px; height: 62px; border-radius: 50%;
    background: var(--green);
  }
  .brand-name {
    font-family: "Questrial", sans-serif;
    font-size: 46px; color: var(--charcoal); letter-spacing: -0.5px;
  }
  .headline {
    position: absolute; left: 50px; top: 196px;
    font-family: "Poppins", sans-serif; font-weight: 700;
    font-size: 41px; line-height: 52px; color: var(--paper);
    letter-spacing: -0.5px;
    text-shadow: 2px 3px 4px rgba(0,0,0,.35);
  }
  .subline {
    position: absolute; left: 51px; top: 312px;
    font-size: 27px; line-height: 31px; color: var(--charcoal);
  }
  .offer-tab {
    position: absolute; left: 50px; top: 429px;
    width: 449px; height: 52px;
    border-radius: 10px 10px 0 0;
    background: linear-gradient(90deg, #f2f2f2, var(--tab));
    text-align: center;
    font-family: "Poppins", sans-serif; font-weight: 600;
    font-size: 30px; line-height: 54px; color: var(--green);
    letter-spacing: -0.5px;
  }
  .call-line {
    position: absolute; left: 58px; top: 479px;
    font-family: "Poppins", sans-serif; font-weight: 600;
    font-size: 31px; line-height: 42px; color: var(--paper);
    letter-spacing: -0.5px;
    text-shadow: 2px 2px 3px rgba(0,0,0,.4);
  }
  .contacts {
    position: absolute; left: 50px; top: 541px;
    list-style: none;
  }
  .contacts li {
    display: flex; align-items: center; gap: 13px;
    height: 33px;
    font-family: "Poppins", sans-serif; font-weight: 600;
    font-size: 21px; color: var(--ink);
  }
  .contact-icon {
    width: 28px; height: 28px; border-radius: 50%;
    background: var(--green);
    display: flex; align-items: center; justify-content: center;
  }
  .portrait {
    position: absolute; left: 622px; top: 12px;
    width: 318px; height: 621px;
    background: radial-gradient(ellipse at 50% 30%, var(--photo-light) 0%, #5a5a5a 45%, var(--photo-dark) 100%);
    border-radius: 150px 150px 0 0;
  }
  .name-tag {
    position: absolute; left: 546px; top: 445px;
    width: 218px; height: 40px;
    background: var(--green);
    clip-path: polygon(0 0, 100% 0, 96% 100%, 0 100%);
    font-family: "Poppins", sans-serif; font-weight: 600;
    font-size: 26px; line-height: 42px; color: var(--paper);
    padding-left: 10px; letter-spacing: -0.3px;
  }
</style>
</head>
<body>
  <main class="banner">
    <svg class="banner-shapes" viewBox="0 0 950 633" width="950" height="633" aria-hidden="true">
      <!-- top charcoal swoosh -->
      <path fill="var(--charcoal)" d="M0 105 C90 128 170 140 250 138 C400 134 560 92 670 89 C780 86 880 120 950 157 L950 192 C880 150 780 118 670 116 C560 116 400 170 250 170 C160 170 80 150 0 134 Z"/>
      <!-- green field -->
      <path fill="var(--green)" d="M0 134 C80 150 160 170 250 170 C400 170 560 116 670 116 C780 118 880 150 950 192 L950 464 C820 500 700 520 600 522 C420 524 200 490 0 500 Z"/>
      <!-- bottom charcoal swoosh -->
      <path fill="var(--charcoal)" d="M0 500 C200 490 420 524 600 522 C700 520 820 500 950 464 L950 522 C830 540 720 545 620 543 C420 540 200 530 0 545 Z"/>
      <!-- call band -->
      <rect x="0" y="479" width="499" height="40" fill="var(--charcoal)"/>
    </svg>

    <div class="brand">
      <span class="brand-dot"></span>
      <span class="brand-name">Campus Lantern</span>
    </div>

    <h1 class="headline">MASTERING THE COLLEGE<br>ADMISSION PROCESS</h1>

    <p class="subline">with personalized, professional guidance<br>in planning, selecting, and applying<br>to the right colleges.</p>

    <div class="offer-tab">FREE CONSULTATION</div>
    <div class="call-line">CALL 555-010–GRAD (4723)</div>

    <ul class="contacts">
      <li>
        <span class="contact-icon">
          <svg viewBox="0 0 16 16" width="16" height="16" aria-hidden="true">
            <g fill="none" stroke="#4a4a4c" stroke-width="1.2">
              <circle cx="8" cy="8" r="6.5"/>
              <ellipse cx="8" cy="8" rx="3" ry="6.5"/>
              <line x1="1.5" y1="8" x2="14.5" y2="8"/>
              <line x1="2.5" y1="4.7" x2="13.5" y2="4.7"/>
              <line x1="2.5" y1="11.3" x2="13.5" y2="11.3"/>
            </g>
          </svg>
        </span>
        www.mycampuslantern.example
      </li>
      <li>
        <span class="contact-icon">
          <svg viewBox="0 0 16 16" width="15" height="15" aria-hidden="true">
            <rect x="1.5" y="3.5" width="13" height="9" fill="#4a4a4c"/>
            <path d="M1.5 3.5 L8 9 L14.5 3.5" fill="none" stroke="#8cc63f" stroke-width="1"/>
          </svg>
        </span>
        nora@mycampuslantern.example
      </li>
    </ul>

    <div class="portrait" role="img" aria-label="Black and white portrait of the consultant, smiling with arms crossed"></div>

    <div class="name-tag">NORA BELLAMY</div>
  </main>
</body>
</html>
```